Values and Organizational Purpose Signage

We recently solidified our company values, organizatioanal purpose and strategic vision. I'd like to develop some tasteful (not overly corporate) signage of these values to display in our office.

I've attached the hand-written values and purpose that my core team members then initialed acknowleding they align along with the signage at the front of our office to provide some perspective on our brand identity.

Industry/Entity Type

It Company

Font styles to use
Sans Serif

Requirements
Must have
• I'd like to see the values and org purpose depicted as one sign and as separate signs (i.e., values on one sign and org purpose on another). I need it to reflect our brand identity which I've uploaded

```html
<!DOCTYPE html>
<html lang="en">
<head>
<meta charset="UTF-8">
<title>Core Values Sign</title>
<link rel="stylesheet" href="https://fonts.googleapis.com/css2?family=Caladea:wght@400&display=swap">
<style>
  :root {
    --lime: #c3d62c;
    --slate: #4a4a4c;
    --white: #ffffff;
    --page: #ffffff;
  }
  html, body {
    margin: 0;
    padding: 0;
    overflow: hidden;
  }
  body {
    width: 740px;
    height: 1200px;
    background: var(--page);
    position: relative;
    font-family: "Caladea", Georgia, serif;
  }
  .values-sign {
    position: absolute;
    left: 27px;
    top: 18px;
    width: 684px;
    height: 1056px;
    background: var(--lime);
  }
  .sign-title {
    position: absolute;
    left: 36px;
    top: 71px;
    margin: 0;
    font-weight: 400;
    font-size: 63px;
    line-height: 85px;
    color: var(--slate);
  }
  .title-rule {
    position: absolute;
    left: 30px;
    top: 254px;
    width: 363px;
    height: 3px;
    background: var(--white);
  }
  .value-name {
    position: absolute;
    left: 36px;
    margin: 0;
    font-weight: 400;
    font-size: 56px;
    line-height: 1;
    color: var(--slate);
  }
  .value-text {
    position: absolute;
    left: 40px;
    width: 620px;
    margin: 0;
    font-size: 31px;
    line-height: 43px;
    color: var(--white);
  }
  .respect-name { top: 297px; }
  .respect-text { top: 359px; }
  .integrity-name { top: 501px; }
  .integrity-text { top: 571px; }
  .excellence-name { top: 652px; }
  .excellence-text { top: 725px; }
  .openness-name { top: 833px; }
  .openness-text { top: 898px; }
  .closing-rule {
    position: absolute;
    left: 542px;
    top: 996px;
    width: 121px;
    height: 3px;
    background: var(--white);
  }
  .brand-name {
    position: absolute;
    left: 0;
    width: 740px;
    top: 1117px;
    text-align: center;
    font-size: 30px;
    line-height: 40px;
    color: var(--slate);
  }
</style>
</head>
<body>
  <section class="values-sign">
    <h1 class="sign-title">Core Values<br>Defines</h1>
    <div class="title-rule"></div>

    <h2 class="value-name respect-name">Respect</h2>
    <p class="value-text respect-text">We are transparent and receptive to the thoughts, opinions, and feelings to others</p>

    <h2 class="value-name integrity-name">Integrity</h2>
    <p class="value-text integrity-text">We uphold our promises</p>

    <h2 class="value-name excellence-name">Excellence</h2>
    <p class="value-text excellence-text">We continuously strive to be the best in all endeavors</p>

    <h2 class="value-name openness-name">Open mindedness</h2>
    <p class="value-text openness-text">We encourage creative and innovative expressions</p>

    <div class="closing-rule"></div>
  </section>

  <div class="brand-name">Norvane</div>
</body>
</html>
```